Conflict prevention NGO needs business cards ASAP

We are a small NGO based in New Caledonia working on conflict prevention, and will be attending a OGA-sponsored conference on small arms next month. Our work involves campaigning against the proliferation of small arms in this post-conflict South Pacific island, and we need business cards to match that purpose.
Our three basic guidelines are the following:
1. We would like the logo of our organisation (see attached) included on this card. We are open to a redesign of this logo to something more stylised or abstract.
2. The card would need to be double-sided: one side in French, the other in English. The text should ideally be minimalist, uncluttered, clear and concise. We prefer the card to visually communicate our mission. As such, we would like the card to present a central image or logo, which would give us the option of printing a texture onto that image/logo later.
3. I have attached images which might inspire the designer (bullets and the famous knotted gun statue). However, these are NOT prescriptive; they are simply thematic ideas, and designers should use their own creative license. We only ask that the overall business card communicate professionalism and a seriousness of purpose, rather than sentimentalism or idealism.
Thanks to everyone who is willing to offer up a design idea! I am grateful for your time, and look forward to viewing your ideas. I apologise, but this has to be a rush job. Please get in touch if you need further guidance.
Please note that our new website will go live on Wednesday evening (Brisbane time), in case it can provide inspiration: http://www.portlumineux.org/
ENGLISH SIDE
[Name, Position] Kieran Vasko, Director
[Organisation] The Centre for a Bright Harbour
[Sub-Title] The first New Caledonian think tank
[Tel] +61407913222
[Email] centreportlumineux@postvale.net
[Website] http://www.portlumineux.org/
FRENCH SIDE
[Name, Position] Kieran Vasko, Directeur
[Organisation] Le Centre pour le Port Lumineux
[Sub-Title] Le premier pôle de réflexion calédonien
[Tel] +61407913222
*Note: We are flexible on the exact way you present the above information, and you may wish to use icons instead of "Tel." for example.

```html
<!DOCTYPE html>
<html lang="en">
<head>
<meta charset="utf-8">
<title>Bright Harbour Business Cards</title>
<link href="https://fonts.googleapis.com/css2?family=Roboto+Condensed:wght@400;700&display=swap" rel="stylesheet">
<style>
  :root {
    --page-bg: #ebebeb;
    --card-bg: #ffffff;
    --brand-blue: #1f4f9c;
    --accent-red: #e02323;
    --contact-green: #3aa53a;
    --photo-dark-a: #2a1c1c;
    --photo-dark-b: #8a6a3a;
    --photo-green-a: #2f6a22;
    --photo-green-b: #6a7480;
  }
  * { margin: 0; padding: 0; box-sizing: border-box; }
  html, body {
    width: 1200px;
    height: 972px;
    overflow: hidden;
    background: var(--page-bg);
    font-family: "Roboto Condensed", "Arial Narrow", sans-serif;
  }
  .card {
    position: absolute;
    width: 540px;
    height: 309px;
    background: var(--card-bg);
    box-shadow: 0 6px 18px rgba(0,0,0,0.15);
    overflow: hidden;
  }
  .card--english { left: 40px; top: 200px; }
  .card--french { left: 620px; top: 463px; }
  .card__photo {
    position: absolute;
    left: 0; top: 0;
    width: 540px; height: 309px;
  }
  .card__info {
    position: absolute;
    left: 58px;
    top: 58px;
    width: 300px;
    text-align: center;
  }
  .brand {
    display: flex;
    align-items: center;
    justify-content: center;
    gap: 10px;
    margin-bottom: 16px;
  }
  .brand__square {
    width: 46px; height: 46px;
    background: var(--brand-blue);
  }
  .brand__name {
    color: var(--brand-blue);
    font-weight: 700;
    font-size: 22px;
  }
  .holder {
    color: var(--brand-blue);
    font-size: 19px;
    line-height: 1.15;
  }
  .holder__name { font-weight: 700; }
  .holder__divider { margin: 0 6px; }
  .tagline {
    color: var(--accent-red);
    font-weight: 700;
    font-size: 18px;
    margin-top: 12px;
  }
  .contacts {
    list-style: none;
    margin-top: 6px;
    color: var(--contact-green);
    font-size: 17px;
    line-height: 1.4;
  }
  .contacts li {
    display: flex;
    align-items: center;
    justify-content: center;
    gap: 7px;
  }
  .contacts svg { width: 14px; height: 14px; flex: none; }
</style>
</head>
<body>

<section class="card card--english" lang="en">
  <svg class="card__photo" viewBox="0 0 540 309" role="img" aria-label="Photograph of rifle cartridges and a shotgun shell">
    <defs>
      <linearGradient id="ammoTones" x1="0" y1="0" x2="1" y2="1">
        <stop offset="0" stop-color="var(--photo-dark-a)"/>
        <stop offset="0.6" stop-color="var(--photo-dark-b)"/>
        <stop offset="1" stop-color="#7a1a1a"/>
      </linearGradient>
    </defs>
    <path d="M290,0 H540 V215 C420,222 315,130 290,0 Z" fill="url(#ammoTones)"/>
  </svg>
  <div class="card__info">
    <div class="brand"><span class="brand__square"></span><span class="brand__name">Bright Harbour</span></div>
    <p class="holder"><span class="holder__name">Kieran Vasko</span><span class="holder__divider">|</span>Director</p>
    <p class="holder">The Centre for a Bright Harbour</p>
    <p class="tagline">The first New Caledonian think tank</p>
    <ul class="contacts">
      <li><svg viewBox="0 0 14 14"><circle cx="7" cy="7" r="7" fill="currentColor"/><path d="M4.5 3.5l1.5 1.5-.8 1c.6 1.2 1.4 2 2.6 2.6l1-.8 1.5 1.5-1 1.2c-2.8-.5-5.3-3-5.8-5.8z" fill="#fff"/></svg>+61407913222</li>
      <li><svg viewBox="0 0 14 14"><circle cx="7" cy="7" r="6.3" fill="none" stroke="currentColor" stroke-width="1.3"/><rect x="3.5" y="4.8" width="7" height="4.6" fill="none" stroke="currentColor" stroke-width="1"/><path d="M3.5 4.8l3.5 2.6 3.5-2.6" fill="none" stroke="currentColor" stroke-width="1"/></svg>centreportlumineux@postvale.net</li>
      <li><svg viewBox="0 0 14 14" fill="none" stroke="currentColor" stroke-width="1.1"><circle cx="7" cy="7" r="6"/><ellipse cx="7" cy="7" rx="2.6" ry="6"/><path d="M1 7h12M2 4h10M2 10h10"/></svg>www.portlumineux.org</li>
    </ul>
  </div>
</section>

<section class="card card--french" lang="fr">
  <svg class="card__photo" viewBox="0 0 540 309" role="img" aria-label="Photograph of a knotted revolver sculpture against green trees">
    <defs>
      <linearGradient id="sculptureTones" x1="0" y1="0" x2="1" y2="1">
        <stop offset="0" stop-color="var(--photo-green-a)"/>
        <stop offset="0.55" stop-color="var(--photo-green-b)"/>
        <stop offset="1" stop-color="#3d7a2a"/>
      </linearGradient>
    </defs>
    <path d="M290,0 H540 V215 C420,222 315,130 290,0 Z" fill="url(#sculptureTones)"/>
  </svg>
  <div class="card__info">
    <div class="brand"><span class="brand__square"></span><span class="brand__name">Bright Harbour</span></div>
    <p class="holder"><span class="holder__name">Kieran Vasko</span><span class="holder__divider">|</span>Director</p>
    <p class="holder">The Centre for a Bright Harbour</p>
    <p class="tagline">Le premier pôle de réflexion calédonien</p>
    <ul class="contacts">
      <li><svg viewBox="0 0 14 14"><circle cx="7" cy="7" r="7" fill="currentColor"/><path d="M4.5 3.5l1.5 1.5-.8 1c.6 1.2 1.4 2 2.6 2.6l1-.8 1.5 1.5-1 1.2c-2.8-.5-5.3-3-5.8-5.8z" fill="#fff"/></svg>+61407913222</li>
      <li><svg viewBox="0 0 14 14"><circle cx="7" cy="7" r="6.3" fill="none" stroke="currentColor" stroke-width="1.3"/><rect x="3.5" y="4.8" width="7" height="4.6" fill="none" stroke="currentColor" stroke-width="1"/><path d="M3.5 4.8l3.5 2.6 3.5-2.6" fill="none" stroke="currentColor" stroke-width="1"/></svg>centreportlumineux@postvale.net</li>
      <li><svg viewBox="0 0 14 14" fill="none" stroke="currentColor" stroke-width="1.1"><circle cx="7" cy="7" r="6"/><ellipse cx="7" cy="7" rx="2.6" ry="6"/><path d="M1 7h12M2 4h10M2 10h10"/></svg>www.portlumineux.org</li>
    </ul>
  </div>
</section>

</body>
</html>
```